Aloe Vera Skin Care Design

Looking to update our 3 Aloe Vera products design, looking for something vibrant and refreshing that you would associate with the skin care product.
A complete front and rear label are required to replace those shown on the attached images, using all text presented in word document. Keep style of 'VARUMEK' the same please.

Current design of 3 products and required text is attached

Colors

Designer to choose colors to be used in the design.

Requirements
Must have
• A complete front and rear label are required to replace those shown on the attached images, using all text presented in word document. Keep style of 'VARUMEK' the same please.

```html
<!DOCTYPE html>
<html lang="en">
<head>
<meta charset="utf-8">
<title>Varumek Aloe Vera Gel – Front and Rear Labels</title>
<link rel="stylesheet" href="https://fonts.googleapis.com/css2?family=Barlow:wght@400;600;700&family=Michroma&family=Roboto+Condensed:wght@400;500;700&family=Yellowtail&display=block">
<style>
  :root {
    --bg: #ffffff;
    --label: #f7f3f8;
    --forest: #0b4a2b;
    --leaf: #64a85d;
    --leaf-light: #9bd67a;
    --leaf-deep: #3f9b45;
    --ink: #1b1b1b;
    --paper: #ffffff;
  }
  * { box-sizing: border-box; margin: 0; padding: 0; }
  html, body { width: 1200px; height: 942px; overflow: hidden; background: var(--bg); }
  .canvas { position: relative; width: 1200px; height: 942px; }

  .label {
    position: absolute; top: 70px; width: 327px; height: 796px;
    background: var(--label);
    border-radius: 164px 164px 0 0 / 150px 150px 0 0;
  }
  .label::after {
    content: ""; position: absolute; inset: 5px;
    border: 1.5px solid var(--forest);
    border-radius: 159px 159px 0 0 / 145px 145px 0 0;
    pointer-events: none;
  }
  .label--front { left: 253px; }
  .label--rear { left: 620px; }

  .brand {
    position: absolute; left: 0; right: 0; text-align: center;
    font-family: "Michroma", sans-serif; color: var(--ink); letter-spacing: -1px;
  }
  .label--front .brand { top: 88px; font-size: 33px; }
  .label--rear .brand { top: 54px; font-size: 22px; }

  .product-title {
    position: absolute; left: 0; right: 0; text-align: center;
    font-family: "Roboto Condensed", sans-serif; font-weight: 700; line-height: 1;
  }
  .product-title__line1 { display: block; color: var(--forest); font-size: 53px; letter-spacing: 2px; }
  .product-title__line2 { display: block; color: var(--leaf); font-size: 64px; margin-top: 6px; letter-spacing: 3px; }
  .label--front .product-title { top: 242px; }

  .claim {
    position: absolute; left: 24px; top: 422px; width: 281px; height: 70px;
    background: var(--forest); box-shadow: 3px 3px 0 #c9d6cc;
    color: #fff; font-family: "Yellowtail", cursive; font-size: 50px;
    display: flex; align-items: center; justify-content: center;
  }

  .divider-dashed { position: absolute; left: 7px; right: 7px; border-top: 1.5px dashed var(--forest); }

  .natural { position: absolute; left: 11px; top: 551px; display: flex; align-items: center; gap: 6px; z-index: 2; }
  .natural__pct {
    background: var(--forest); color: #fff; width: 72px; height: 42px;
    font-family: "Roboto Condensed", sans-serif; font-weight: 500; font-size: 36px;
    display: flex; align-items: center; justify-content: center;
  }
  .natural__text { font-family: "Roboto Condensed", sans-serif; color: var(--leaf); line-height: 1; }
  .natural__text b { display: block; font-size: 22px; letter-spacing: 1px; }
  .natural__text span { display: block; font-size: 14px; margin-top: 3px; }

  .tagline-band {
    position: absolute; left: 7px; right: 7px; top: 607px; height: 106px;
    background: var(--leaf); border-top: 3px solid var(--forest);
    color: #fff; font-family: "Roboto Condensed", sans-serif; font-weight: 400;
    font-size: 22px; line-height: 24px; padding: 14px 0 0 12px;
  }
  .plant-art {
    position: absolute; left: 170px; top: 538px; width: 150px; height: 172px;
    background: radial-gradient(ellipse 60% 55% at 60% 45%, var(--leaf-light) 0%, var(--leaf-deep) 55%, rgba(100,168,93,0) 100%);
  }
  .rule-double { position: absolute; left: 7px; right: 7px; top: 716px; height: 7px; border-top: 3px solid var(--forest); border-bottom: 1.5px solid var(--forest); }
  .volume {
    position: absolute; left: 0; right: 0; top: 742px; text-align: center;
    font-family: "Barlow", sans-serif; font-size: 29px; color: var(--ink);
  }

  .rear-heading {
    position: absolute; left: 49px; width: 231px; top: 117px; height: 36px;
    background: var(--leaf); color: #fff;
    font-family: "Roboto Condensed", sans-serif; font-weight: 700; font-size: 26px; letter-spacing: 1px;
    display: flex; align-items: center; justify-content: center;
    outline: 1.5px dashed var(--forest); outline-offset: 1px;
  }
  .rear-copy {
    position: absolute; left: 24px; right: 24px; top: 164px; text-align: center;
    font-family: "Barlow", sans-serif; font-size: 16.5px; line-height: 23px; color: var(--ink);
  }
  .ingredients-heading {
    position: absolute; left: 82px; width: 165px; top: 291px; height: 23px;
    background: var(--forest); color: #fff;
    font-family: "Barlow", sans-serif; font-weight: 600; font-size: 18px; letter-spacing: .5px;
    display: flex; align-items: center; justify-content: center;
  }
  .ingredients {
    position: absolute; left: 26px; right: 26px; top: 331px; text-align: center;
    font-family: "Barlow", sans-serif; font-size: 13.6px; line-height: 18.7px; color: var(--ink);
  }
  .distributor {
    position: absolute; left: 33px; top: 497px; font-style: normal;
    font-family: "Barlow", sans-serif; font-size: 14px; line-height: 19px; color: var(--ink);
  }
  .distributor strong { font-size: 16px; font-weight: 700; }
  .distributor-mark {
    position: absolute; left: 196px; top: 566px; display: flex; align-items: center; gap: 5px;
    font-family: "Barlow", sans-serif; font-weight: 700; font-size: 15px; color: var(--ink);
  }
  .distributor-mark__dot { width: 12px; height: 12px; border-radius: 50%; background: #e21b23; }
  .item-no { position: absolute; left: 33px; top: 628px; font-family: "Barlow", sans-serif; font-size: 14px; color: var(--ink); }
  .code-box { position: absolute; left: 54px; top: 667px; width: 222px; height: 82px; background: var(--paper); border: 1.5px solid #333; }
</style>
</head>
<body>
<main class="canvas">

  <section class="label label--front" aria-label="Front label">
    <div class="brand">VARUMEK</div>
    <h1 class="product-title">
      <span class="product-title__line1">ALOE VERA</span>
      <span class="product-title__line2">GEL</span>
    </h1>
    <div class="claim">Non Oily</div>
    <div class="divider-dashed" style="top:542px"></div>
    <div class="natural">
      <div class="natural__pct">98%</div>
      <div class="natural__text"><b>NATURAL</b><span>ALOE VERA GEL</span></div>
    </div>
    <div class="tagline-band">Skin Care<br>From Natures<br>Wonder Plant</div>
    <div class="plant-art" role="img" aria-label="Illustration of an aloe vera plant rising from water"></div>
    <div class="rule-double"></div>
    <div class="volume">150ml</div>
  </section>

  <section class="label label--rear" aria-label="Rear label">
    <div class="brand">VARUMEK</div>
    <h2 class="rear-heading">ALOE VERA GEL</h2>
    <p class="rear-copy">Aloe Vera is a natural substance derived from the sap of the Aloe Vera plant. Use Aloe Vera Gel for the relief of sunburn , minor cuts and burns and dry skins.</p>
    <h3 class="ingredients-heading">INGREDIENTS</h3>
    <p class="ingredients">Water (Aqua), Alcohol, Glycerin, Aloe Barbadensis Leaf Extract, PEG-40 Hydrogenated Castor Oil, Phenoxyeth-anol, Propylene Glycol, Diazolidinyl Urea, Iodopropynyl Butylcarbamate, Carbomer, Triethanolamine, Fragrance, Yellow 5 CI19140, Blue 1 CI42090.</p>
    <div class="divider-dashed" style="top:479px; left:30px; right:30px"></div>
    <address class="distributor">
      DISTRIBUTED BY<br>
      <strong>Greenleaf Pty Limited</strong><br>
      12-14 MARLOW STREET<br>
      CARDEN NSW 2301<br>
      Made in Austrlia<br>
      www.greenleafco.com.au
    </address>
    <div class="distributor-mark"><span class="distributor-mark__dot"></span>GREENLEAF</div>
    <div class="item-no">Item No: GL318</div>
    <div class="code-box"></div>
  </section>

</main>
</body>
</html>
```